Etiketten-Design für Fruchtsaft-Schorlen und Cider
Wir sind total happy mit dem, was wir bekommen haben. Insgesamt fünf Designs, die absolut top waren und super gepasst haben. Wir hatten das Luxusproblem uns für eines der fünf zu entscheiden. Weil die Qualität dermaßen gut war, haben wir uns entschieden nochmals den Betrag des Preisgelds in die Hand zu nehmen und auf Platz 2 bis 4 unseres internen Rankings zu verteilen. Nämlich die Hälfte auf Platz 2 und jeweils ein Viertel auf die beiden dritten Plätze.
Zielgruppe
Wir sind ein landwirtschaftlicher Betrieb mit Fokus auf den Hochstamm-Feldobstbau, landläufig Streuobst genannt. Wir sind in Tübingen gelegen, im Zentrum des Talgrunder Baumwiesenverbunds (1).
Unsere Obsternte verarbeiten wir zu Fruchtsaft-Schorlen und Cider. Unter den Getränkeherstellern sind wir ein mikrokleiner Zwerg. Allerdings wird die Qualität unserer Getränke überragend hoch gelobt. Dazu trägt in wesentlichem Maße die außerordentliche Fruchtgüte unserer oftmals mehr als hundert Jahre alten Apfel- und Birnbäume bei. Deren altbewährten Sorten haben sich seit Generationen als besonders geeignet für die Saft- und Obstwein-Produktion erwiesen. Auch bei den zahlreichen Neupflanzung setzen wir nur auf diese traditionellen Sorten.
Für unser neues Produkt 'Mostschorle' benötigen wir Flaschenetiketten, ein Bauchetikett und ein Rückenetikett.
Most, zur Erklärung, ist die schwäbische Variante des Apfelweins. Weitere regionale Varianten: Hessen Ebbelwoi, Saarland Viez, Frankreich Cidre, Spanien Sidra und im angelsächsischen Sprachraum Cider. Im Gegensatz zu Apfelwein wird Schwäbischer Most nicht allein aus Äpfeln sondern aus einer Mischung von Äpfeln, Birnen und (manchmal) Quitten gemacht.
Most hat ein sehr schlechtes Image. Einstmals das Volksgetränk schlechthin, mittlerweile praktisch bedeutungslos. Dies nicht ganz unverschuldet, weil oft in sehr nachlässiger Art hergestellt. Unser Most ist tadellos gut und hat das Potential Freunde zurückzugewinnen oder neu zu gewinnen.
Unsere Zielgruppe sind alle, die ein leicht alkoholisches Getränk möchten; Beispiel Weinschorle. Der Vertrieb beschränkt sich auf unser lokales Einzugsgebiet, ergänzt durch ein wenig Internetvertrieb.
Um sich in's Produkt eingrooven zu können verschicken wir gerne eine Kostprobe - nachdem eine Etiketten-Arbeitsprobe vorliegt, die gefällt. :-)
Mehr Info:
(1) https://www.talgrund-wiesenbund.de/
(2)https://www.k..
Aufgabenstellung
Die neuen Etiketten dürfen anders oder völlig anders aussehen als die Etiketten unserer bereits vorhandenen Produkte. Als Inspiration gerne Cider- und/oder Biermarken heranziehen. Firmenfarbe grün soll berücksichtigt werden. Firmenschrift Garamond weitgehend ebenso. Wenn runde oder ovale Gestaltung, dann auf einem rechteckigem Fond, weil wir nur rechteckige Etiketten verarbeitet werden können.
Bei der betreffenden Flasche handelt es sich um die weit verbreitete 0,33-Liter-Longneck-Flasche, Glasfarbe braun.
Flaschenverschluß durch Kronkorken. Es kann unter folgenden Kronkorken-Farben gewählt werden: silber, altgold, gelb, weiß, rot, orange, schwarz.
Grafikdateien sind beigefügt für: Firmenlogo, Unterstützer-Logos, Nährwerte-QR-Code, Mehrweg-Logo, Barcode
Texte und Inhalte für Rückenetikett siehe beigefügte Datei.
Zum Bauchetikett haben wir kein Briefing gemacht, um der Kreativität freien Lauf zu lassen.
Technische Angaben zu den Etiketten:
Abmessung Bauchetikett: 85mm hoch x 80 mm breit
Abmessung Rückenetikett: 70mm hoch x 60mm breit

```html
<!DOCTYPE html>
<html lang="de">
<head>
<meta charset="utf-8">
<title>Hangwieser Cider – Bauchetikett</title>
<link rel="stylesheet" href="https://fonts.googleapis.com/css2?family=EB+Garamond:wght@400;500&display=swap">
<style>
  :root {
    --page: #ffffff;
    --label-top: #1f201f;
    --label-mid: #25452f;
    --label-bottom: #10772e;
    --frame: #c8c8c6;
    --brand-green: #1a7d32;
    --accent-lime: #8cc63f;
    --leaf: #6f9a4e;
    --fruit: #4e8c3a;
    --ink-light: #e4e4e2;
  }
  html, body {
    margin: 0;
    width: 1199px;
    height: 1200px;
    overflow: hidden;
    background: var(--page);
  }
  .stage {
    position: relative;
    width: 1199px;
    height: 1200px;
  }
  .belly-label {
    position: absolute;
    left: 229px;
    top: 207px;
    width: 741px;
    height: 787px;
    display: block;
  }
  .label-text {
    font-family: "EB Garamond", Garamond, serif;
    text-anchor: middle;
  }
  .brand-name { fill: var(--brand-green); font-size: 54px; font-weight: 500; }
  .product-name { fill: var(--frame); font-size: 140px; letter-spacing: 10px; }
  .origin-line { fill: var(--ink-light); font-size: 33px; }
  .fact { fill: var(--ink-light); font-size: 34px; }
</style>
</head>
<body>
<main class="stage">
  <svg class="belly-label" viewBox="0 0 927 985" xmlns="http://www.w3.org/2000/svg">
    <defs>
      <linearGradient id="label-fond" x1="0" y1="0" x2="0" y2="1">
        <stop offset="0" stop-color="var(--label-top)"/>
        <stop offset="0.25" stop-color="var(--label-top)"/>
        <stop offset="0.55" stop-color="var(--label-mid)"/>
        <stop offset="0.85" stop-color="var(--label-bottom)"/>
        <stop offset="1" stop-color="var(--label-bottom)"/>
      </linearGradient>
    </defs>

    <rect class="label-fond" width="927" height="985" fill="url(#label-fond)"/>

    <path class="fruit-motif" role="img" aria-label="Angedeutete Apfel-Silhouette"
      d="M500 660 C495 560 560 480 640 470 C700 465 760 490 780 540 L780 850 L540 850 C510 780 500 720 500 660 Z"
      fill="var(--fruit)" opacity="0.75"/>

    <g class="frame" fill="none" stroke="var(--frame)">
      <path class="frame-outer" stroke-width="9"
        d="M250 150 A340 340 0 0 1 677 150 M307 152 L175 152 Q160 175 140 184 L140 812 Q165 820 178 844 L318 844 M607 844 L749 844 Q762 820 787 812 L787 184 Q767 175 752 152 L617 152 M262 844 A330 330 0 0 0 665 844"/>
      <path class="frame-inner" stroke-width="3"
        d="M278 150 A320 320 0 0 1 650 150 M292 167 L190 167 Q178 190 160 200 L160 797 Q180 806 192 830 L300 830 M625 830 L735 830 Q747 806 767 797 L767 200 Q749 190 737 167 L630 167 M280 862 A310 310 0 0 0 648 862"/>
    </g>

    <g class="ornament-placeholders" role="img" aria-label="Schwung-Ornamente und Blätter" fill="var(--frame)" opacity="0.7">
      <rect x="197" y="206" width="58" height="5" rx="2.5"/>
      <rect x="677" y="206" width="58" height="5" rx="2.5"/>
      <rect x="197" y="784" width="58" height="5" rx="2.5"/>
      <rect x="677" y="784" width="58" height="5" rx="2.5"/>
      <ellipse cx="466" cy="296" rx="30" ry="11" fill="var(--leaf)" opacity="1"/>
      <ellipse cx="462" cy="514" rx="34" ry="11" fill="var(--leaf)" opacity="1"/>
      <ellipse cx="462" cy="880" rx="34" ry="11" fill="var(--leaf)" opacity="1"/>
    </g>

    <text class="label-text brand-name" x="464" y="205">Hangwieser</text>

    <path class="accent-swash" d="M302 320 Q464 350 628 320" stroke="var(--accent-lime)" stroke-width="4" fill="none"/>
    <text class="label-text product-name" x="464" y="452">Cider</text>
    <path class="accent-swash" d="M312 490 Q464 455 622 490" stroke="var(--accent-lime)" stroke-width="4" fill="none"/>

    <text class="label-text origin-line" x="460" y="620">Aus heimischen Äpfeln und Birnen</text>
    <text class="label-text origin-line" x="460" y="664">traditionell bewirtschafteter</text>
    <text class="label-text origin-line" x="460" y="708">Streuobstwiesen</text>

    <text class="label-text fact" x="362" y="792">℮ 0,33 l</text>
    <line class="fact-divider" x1="462" y1="742" x2="462" y2="812" stroke="var(--ink-light)" stroke-width="2"/>
    <text class="label-text fact" x="576" y="792">3% Vol.</text>
  </svg>
</main>
</body>
</html>
```